New business card for civil engineering company - "Keel Survey"

We need a business card designed for our new structural engineering company.

The company name is "Keel Survey" logo files attached.

We would like the following:
* Two-sided card
* Simple design

Information to be placed on the card:
Name - Marcus Hollby
Job Title - Director / Structural Engineer
Credentials - BEng(Hons), CPEng, CMengNZ, IntPE(NZ)
Email - marcus.hollby@keelsurvey-example.co.nz
mobile - 0219036458
website - www.keelsurvey-example.co.nz

```html
<!DOCTYPE html>
<html lang="en">
<head>
<meta charset="utf-8">
<title>Keel Survey – Business Card</title>
<link href="https://fonts.googleapis.com/css2?family=Jost:wght@300;400;600;700&family=Open+Sans:wght@400;600;700&display=swap" rel="stylesheet">
<style>
  :root {
    --navy: #14426f;
    --sky: #06a0e0;
    --ink: #1b1b1b;
    --white: #ffffff;
    --page: #ffffff;
  }
  * { margin: 0; padding: 0; box-sizing: border-box; }
  html, body { width: 1200px; height: 1200px; overflow: hidden; background: var(--page); }
  .canvas { position: relative; width: 1200px; height: 1200px; }

  .card { position: absolute; background: var(--white); overflow: hidden;
          box-shadow: 0 6px 14px rgba(0,0,0,.25); }

  /* Front */
  .card--front { left: 154px; top: 68px; width: 894px; height: 510px; }
  .wordmark { position: absolute; display: flex; align-items: center; gap: 12px;
              font-family: "Jost", sans-serif; font-weight: 600; letter-spacing: 3px; }
  .front__wordmark { left: 0; right: 0; top: 210px; justify-content: center;
                     font-size: 34px; color: var(--navy); }
  .front__wordmark .mark { width: 26px; height: 26px; background: var(--navy); }
  .front__band { position: absolute; left: 0; top: 312px; width: 100%; height: 118px;
                 background: var(--navy); display: flex; align-items: center; justify-content: center;
                 font-family: "Jost", sans-serif; font-size: 74px; color: var(--white); gap: 22px; }
  .front__band b { font-weight: 700; }
  .front__band span { font-weight: 300; }
  .url-strip { position: absolute; left: 0; width: 100%; display: flex; align-items: center;
               justify-content: center; color: var(--white); font-family: "Open Sans", sans-serif;
               font-size: 19px; letter-spacing: 5px; }
  .url-strip b { font-weight: 700; }
  .front__url { top: 444px; height: 40px; background: var(--sky); }

  /* Back */
  .card--back { left: 150px; top: 621px; width: 900px; height: 514px; }
  .back__waves { position: absolute; left: 0; top: 0; }
  .back__wordmark { right: 44px; top: 150px; font-size: 19px; color: var(--white); gap: 8px; letter-spacing: 2px; }
  .back__wordmark .mark { width: 14px; height: 14px; background: var(--white); }
  .person { position: absolute; left: 60px; top: 258px; }
  .person__name { font-family: "Jost", sans-serif; font-weight: 700; font-size: 42px;
                  color: var(--navy); line-height: 1; margin-bottom: 22px; }
  .person__role { font-family: "Open Sans", sans-serif; font-size: 20px; color: var(--ink); line-height: 29px; }
  .divider { position: absolute; left: 439px; top: 263px; width: 2px; height: 165px; background: var(--ink); }
  .contacts { position: absolute; left: 478px; top: 284px; list-style: none;
              font-family: "Open Sans", sans-serif; color: var(--ink); }
  .contacts li { display: flex; align-items: center; gap: 16px; height: 42px; font-size: 18px; }
  .contacts li.phone { font-size: 21px; font-weight: 700; }
  .contacts b { font-weight: 700; }
  .contacts svg { width: 26px; height: 26px; flex: none; }
  .back__url { top: 459px; height: 42px; background: var(--navy); }
</style>
</head>
<body>
<div class="canvas">

  <section class="card card--front">
    <div class="wordmark front__wordmark"><i class="mark"></i>KEEL SURVEY</div>
    <div class="front__band"><b>KEEL</b><span>SURVEY</span></div>
    <div class="url-strip front__url">www.<b>keelsurvey-example</b>.co.nz</div>
  </section>

  <section class="card card--back">
    <svg class="back__waves" width="900" height="514" viewBox="0 0 900 514" aria-hidden="true">
      <path fill="var(--navy)" d="M0 0H900V208C820 232 720 240 640 230C480 205 320 92 180 100C100 106 40 122 0 135Z"/>
      <path fill="var(--sky)" d="M0 150C60 130 140 115 220 118C380 126 520 215 680 232C560 236 420 190 260 146C160 120 80 150 0 185Z"/>
    </svg>
    <div class="wordmark back__wordmark"><i class="mark"></i>KEEL SURVEY</div>

    <div class="person">
      <h1 class="person__name">Marcus Hollby</h1>
      <p class="person__role">Director / Structural Engineer<br>Credentials - BEng(Hons), CPEng,<br>CMengNZ, IntPE(NZ)</p>
    </div>

    <div class="divider"></div>

    <ul class="contacts">
      <li class="phone">
        <svg viewBox="0 0 24 24"><path fill="var(--navy)" d="M6.6 10.8a15 15 0 0 0 6.6 6.6l2.2-2.2a1 1 0 0 1 1-.25 11.4 11.4 0 0 0 3.6.57 1 1 0 0 1 1 1V20a1 1 0 0 1-1 1A17 17 0 0 1 3 4a1 1 0 0 1 1-1h3.5a1 1 0 0 1 1 1c0 1.25.2 2.45.57 3.57a1 1 0 0 1-.25 1Z"/></svg>
        0219036458
      </li>
      <li>
        <svg viewBox="0 0 24 24"><circle cx="12" cy="12" r="12" fill="var(--navy)"/><path fill="var(--white)" d="M6 8h12v8H6z"/><path fill="none" stroke="var(--navy)" stroke-width="1.4" d="M6 8l6 5 6-5"/></svg>
        <span>marcus.<b>hollby@keelsurvey-example</b>.co.nz</span>
      </li>
      <li>
        <svg viewBox="0 0 24 24"><g fill="none" stroke="var(--navy)" stroke-width="1.6"><circle cx="12" cy="12" r="10"/><ellipse cx="12" cy="12" rx="4.5" ry="10"/><path d="M2 12h20M4 7h16M4 17h16"/></g></svg>
        <span>www.<b>keelsurvey-example</b>.co.nz</span>
      </li>
    </ul>

    <div class="url-strip back__url">www.<b>keelsurvey-example</b>.co.nz</div>
  </section>

</div>
</body>
</html>
```